Stationery Design Project

Minimal Design. Black and White Colours Only.
Need Business Card
With Compliments slip
Letterhead
A4 Folder

Target Market(s)

Luxury architectual designed home owners

Industry/Entity Type

Business

Requirements
Must have
• Black and White colours only. Suggest some good textured stock for business card for future printing. try to use font that is used in my logo our some other minimal modern font.

```html
<!DOCTYPE html>
<html lang="en">
<head>
<meta charset="utf-8">
<title>Norvale Estates Letterhead</title>
<link rel="stylesheet" href="https://fonts.googleapis.com/css2?family=Montserrat:wght@500;700&family=Lobster+Two:ital,wght@1,700&display=swap">
<style>
  :root {
    --paper: #ffffff;
    --ink: #1a1a1a;
    --rule: #a6a6a6;
    --frame: #9c9c9c;
    --band-grey: #9e9e9e;
    --band-black: #0d0d0d;
    --footer-text: #ffffff;
  }
  * { margin: 0; padding: 0; box-sizing: border-box; }
  html, body {
    width: 928px; height: 1200px; overflow: hidden;
    background: var(--paper);
  }
  .letterhead {
    position: relative; width: 928px; height: 1200px;
    background: var(--paper);
  }
  .page-frame {
    position: absolute; left: 9px; top: 17px; width: 832px; height: 1170px;
    border: 2px solid var(--frame);
    border-top: none;
  }
  .page-frame::before {
    content: ""; position: absolute; left: -2px; right: -2px; top: 0;
    border-top: 2px solid var(--frame);
  }
  .brand {
    position: absolute; left: 40px; top: 56px;
    display: flex; align-items: center; gap: 10px;
    font-family: "Montserrat", sans-serif; font-weight: 500;
    font-size: 19px; letter-spacing: 0.5px; color: var(--ink);
  }
  .brand-mark {
    width: 30px; height: 30px; background: var(--ink);
  }
  .header-rule {
    position: absolute; left: 11px; top: 106px; width: 828px;
    border-top: 3px solid var(--rule);
  }
  .address {
    position: absolute; left: 531px; top: 43px;
    display: flex; align-items: center; gap: 6px;
    font-family: "Lobster Two", cursive; font-style: italic; font-weight: 700;
    font-size: 12px; line-height: 15px; color: var(--ink);
  }
  .address svg { width: 20px; height: 18px; }
  .contact-list {
    position: absolute; left: 674px; top: 28px; list-style: none;
    font-family: "Lobster Two", cursive; font-style: italic; font-weight: 700;
    font-size: 12px; color: var(--ink);
  }
  .contact-list li {
    display: flex; align-items: center; gap: 10px; height: 22px;
  }
  .contact-list svg { width: 20px; height: 20px; flex: none; }
  .footer-band {
    position: absolute; left: 9px; top: 1118px; width: 832px; height: 60px;
  }
  .footer-web {
    position: absolute; left: 591px; top: 1140px;
    display: flex; align-items: center; gap: 8px;
    font-family: "Lobster Two", cursive; font-style: italic; font-weight: 700;
    font-size: 11px; color: var(--footer-text);
  }
  .footer-web svg { width: 16px; height: 16px; }
</style>
</head>
<body>
<main class="letterhead">
  <div class="page-frame"></div>

  <header>
    <div class="brand"><span class="brand-mark"></span>NORVALE ESTATES</div>

    <address class="address">
      <svg viewBox="0 0 20 18" aria-hidden="true"><path d="M10 1 L1 9 H4 V17 H8 V12 H12 V17 H16 V9 H19 Z" fill="var(--ink)"/></svg>
      <span>Level 12, 48 Harbour Rd<br>Carlton VIC 3053<br>Australia</span>
    </address>

    <ul class="contact-list">
      <li>
        <svg viewBox="0 0 20 20" aria-hidden="true"><rect x="5" y="3" width="10" height="16" rx="1.5" fill="none" stroke="var(--ink)" stroke-width="2"/><circle cx="10" cy="1.5" r="1.3" fill="var(--ink)"/></svg>
        <span>+61 400 555 012</span>
      </li>
      <li>
        <svg viewBox="0 0 20 20" aria-hidden="true"><path d="M2 8 Q10 2 18 8 L16 10 L13 8 V7 H7 V8 L4 10 Z" fill="var(--ink)"/><rect x="5" y="10" width="10" height="7" rx="1" fill="var(--ink)"/><circle cx="10" cy="13.5" r="2" fill="#fff"/></svg>
        <span>+61 3 5550 1234</span>
      </li>
      <li>
        <svg viewBox="0 0 20 20" aria-hidden="true"><path d="M2 9 L10 3 L18 9 V18 H2 Z" fill="var(--ink)"/><rect x="5" y="7" width="10" height="8" fill="#fff"/><text x="10" y="14" font-size="7" text-anchor="middle" font-family="Arial, sans-serif" fill="var(--ink)">@</text></svg>
        <span>hello@norvaleestates.com</span>
      </li>
    </ul>
  </header>

  <div class="header-rule"></div>

  <footer>
    <svg class="footer-band" viewBox="0 0 832 60" preserveAspectRatio="none" aria-hidden="true">
      <defs>
        <linearGradient id="bandShade" x1="0" y1="0" x2="1" y2="0">
          <stop offset="0" stop-color="#2a2a2a"/>
          <stop offset="0.5" stop-color="#0d0d0d"/>
          <stop offset="1" stop-color="#1e1e1e"/>
        </linearGradient>
      </defs>
      <rect x="0" y="18" width="832" height="20" fill="var(--band-grey)"/>
      <rect x="0" y="37" width="832" height="18" fill="url(#bandShade)"/>
      <path d="M500 38 C535 36 540 8 580 6 H832 V38 Z" fill="var(--band-black)"/>
    </svg>
    <div class="footer-web">
      <svg viewBox="0 0 16 16" aria-hidden="true"><g fill="none" stroke="#fff" stroke-width="1"><circle cx="8" cy="8" r="7"/><ellipse cx="8" cy="8" rx="3" ry="7"/><line x1="1" y1="8" x2="15" y2="8"/></g></svg>
      <span>www.norvaleestates.com</span>
    </div>
  </footer>
</main>
</body>
</html>
```